Business Card for Marco Thieblin Analytics and Marco Thieblin Photography

I want a double sided business card: on one side it should be about "Marco Thieblin Photography" and on the other side about "Marco Thieblin Analytics". You find the logos for these two projects in the attachments. The design of the business card should blend well with the colours and fonts used in the logos and should be quite simple, yet look professional and modern.

In addition to my name, there should be content for a telephone number, e-mail address and website. There should be little icons (for telephone, email and web) before these fields. I do not want a postal mail address field.
Lastly you should indicate that people can contact me in the following languages: Lëtzebuergesch, Deutsch, Français, English, Castellano, Ido
This should be very unobtrusive: either in a small muted font or with little icons (preferably without using flags as flags represent nations, not languages - one possibility would be by using the 2 letter ISO codes).

The design should be delivered in Adobe Illustrator format or something similar that I can edit easily, as it's possible that I will change my e-mail address and domain soon.

I hope this was detailed enough but still leaves you some freedom for designing something nice.

Thank you!
Marco

Industry/Entity Type

Business

Contact Information for Business Card

e-mail address: mtb_@orvenmail.example
website: www.marcothieblin.example (for Marco Thieblin Photography)
website: kelvodata.example/mtb (for Marco Thieblin Analytics - this address is likely to change)
phone: +352 691 987 654 (not my real number - I prefer not to publish it on the web)

Requirements
Nice to have
• A speech bubble followed by the 2-letter language codes (lb, de, fr, en, es, io) or even speech bubble icons for every language would be nice and eliminates the need to put text like 'you can contact me in the following languages'.

```html
<!DOCTYPE html>
<html lang="en">
<head>
<meta charset="utf-8">
<title>Marco Thieblin Analytics – Business Card</title>
<link href="https://fonts.googleapis.com/css2?family=Open+Sans:wght@400;600;700&display=swap" rel="stylesheet">
<style>
  :root {
    --page-bg: #ffffff;
    --card-bg: #d1d2d4;
    --card-shadow: #58585a;
    --band-dark: #060707;
    --band-slope: #141414;
    --ink: #231f20;
    --brand-orange: #ee8322;
    --green-dark: #0b6a3a;
    --green-light: #7cc143;
    --icon-green: #6cbd4b;
    --bubble-fill: #f4f4f4;
  }
  * { margin: 0; padding: 0; box-sizing: border-box; }
  html, body {
    width: 1200px; height: 1000px; overflow: hidden;
    background: var(--page-bg);
    font-family: "Open Sans", Arial, sans-serif;
  }
  .canvas { position: relative; width: 1200px; height: 1000px; }
  .card-shadow {
    position: absolute; left: 213px; top: 281px; width: 786px; height: 450px;
    background: var(--card-shadow); filter: blur(2px);
  }
  .card {
    position: absolute; left: 207px; top: 275px; width: 786px; height: 450px;
    background: var(--card-bg); overflow: hidden;
  }
  .brand-name {
    position: absolute; left: 0; width: 100%; top: 128px;
    text-align: center; font-size: 32px; font-weight: 600;
    color: var(--brand-orange); letter-spacing: 0.5px;
  }
  .divider-band { position: absolute; left: 0; top: 0; }
  .contact-list { position: absolute; left: 52px; top: 318px; list-style: none; }
  .contact-item {
    position: absolute; left: 0; display: flex; align-items: center;
    font-size: 16px; font-weight: 700; color: var(--ink); white-space: nowrap;
  }
  .contact-item svg { flex: none; }
  .contact-item.phone { top: 0; }
  .contact-item.phone .contact-text { margin-left: 13px; }
  .contact-item.email { top: 42px; }
  .contact-item.email .contact-text { margin-left: 19px; }
  .contact-item.web { top: 90px; }
  .contact-item.web .contact-text { margin-left: 19px; }
  .language-bubble { position: absolute; left: 578px; top: 375px; }
  .language-codes {
    position: absolute; left: 591px; top: 393px;
    font-size: 15px; color: #000; word-spacing: 3px; white-space: nowrap;
  }
</style>
</head>
<body>
<div class="canvas">
  <div class="card-shadow"></div>
  <section class="card" aria-label="Business card, analytics side">
    <p class="brand-name">Marco Thieblin Analytics</p>

    <svg class="divider-band" width="786" height="450" viewBox="0 0 786 450" aria-hidden="true">
      <polygon fill="var(--band-dark)" points="0,215 136,215 136,263 0,263"/>
      <polygon fill="var(--band-slope)" points="136,215 293,263 293,312 136,263"/>
      <polygon fill="var(--band-dark)" points="293,263 493,263 493,312 293,312"/>
      <polygon fill="var(--band-slope)" points="493,263 585,215 585,263 493,312"/>
      <polygon fill="var(--band-dark)" points="585,215 786,215 786,263 585,263"/>
    </svg>

    <ul class="contact-list">
      <li class="contact-item phone">
        <svg width="28" height="28" viewBox="0 0 28 28" fill="none" stroke="var(--icon-green)" stroke-width="1.5" stroke-linecap="round">
          <path d="M6 4l4 4-2.5 3c1.5 3.5 4 6 7.5 7.5l3-2.5 4 4-3 3C12 22 5 15 3 7z"/>
          <path d="M16 4a8 8 0 0 1 8 8"/><path d="M16 8a4 4 0 0 1 4 4"/>
        </svg>
        <span class="contact-text">+352 691 987 654</span>
      </li>
      <li class="contact-item email">
        <svg width="24" height="18" viewBox="0 0 24 18" fill="none" stroke="var(--icon-green)" stroke-width="1.5">
          <rect x="1" y="2" width="22" height="14"/><path d="M1 2l11 8 11-8"/>
        </svg>
        <span class="contact-text">mtb_@orvenmail.example</span>
      </li>
      <li class="contact-item web">
        <svg width="28" height="28" viewBox="0 0 28 28" fill="none" stroke="var(--icon-green)" stroke-width="1.5">
          <circle cx="14" cy="14" r="12"/><ellipse cx="14" cy="14" rx="5" ry="12"/>
          <path d="M2 14h24M4 8h20M4 20h20"/>
        </svg>
        <span class="contact-text">kelvodata.example/mtb</span>
      </li>
    </ul>

    <svg class="language-bubble" width="180" height="75" viewBox="0 0 180 75" aria-hidden="true">
      <defs>
        <linearGradient id="bubbleGreen" x1="0" y1="0" x2="1" y2="0">
          <stop offset="0" stop-color="var(--green-dark)"/>
          <stop offset="1" stop-color="var(--green-light)"/>
        </linearGradient>
      </defs>
      <path fill="#6d6e70" d="M6 5h163a5 5 0 0 1 5 5v36a5 5 0 0 1-5 5h-7l-1 20-14-20H6a5 5 0 0 1-5-5V10a5 5 0 0 1 5-5z"/>
      <path fill="url(#bubbleGreen)" d="M7 2h155a5 5 0 0 1 5 5v35a5 5 0 0 1-5 5h-4l-1 19-12-19H7a5 5 0 0 1-5-5V7a5 5 0 0 1 5-5z"/>
      <rect x="9" y="8" width="151" height="33" rx="6" fill="var(--bubble-fill)"/>
    </svg>
    <p class="language-codes">lb de fr en es io</p>
  </section>
</div>
</body>
</html>
```